Have Logo - Need Business Card Design!!!

I am looking for a business card design for a real estate development business. The company name is Tallowfen Property Group. I already have a logo created by Sketch Harbor and would like this logo to be incorporated into the design. I have uploaded the files. The card needs to be professional, but visually interesting. Not necessary to be double-sided, but if you want to get creative and can think of something to put on the back then have at it.

Target Market(s)

The target audience for these business cards will be professionals in the real estate industry.

Industry/Entity Type

Real Estate

Requirements
Must have
• The business card must have all the necessary items for a business card, i.e. company name, our logo, name (however, not title necessary), office address, office phone number, cell number, fax number, website address, etc.

You can use the information below for the card:

Gregory L. Hanlon
782 Marlowe Avenue
San Francisco, California 94127

www.tallowfengroup.example
ghanlon@tallowfengroup.example
Office: 415-555-0142
Fax: 415-555-0143
Cell: 415-555-0186

```html
<!DOCTYPE html>
<html lang="en">
<head>
<meta charset="utf-8">
<title>Tallowfen Property Group – Business Card</title>
<link rel="stylesheet" href="https://fonts.googleapis.com/css2?family=PT+Sans:wght@400;700&display=swap">
<style>
  :root {
    --green: #0f8a45;
    --navy: #1e3a78;
    --grey: #4a4a4a;
    --paper: #ffffff;
    --backdrop: #ecebe8;
    --tint-green: #cfe5d6;
    --tint-navy: #d3d8e8;
  }
  * { margin: 0; padding: 0; box-sizing: border-box; }
  html, body { width: 1200px; height: 902px; overflow: hidden; }
  body {
    background: var(--backdrop);
    font-family: "PT Sans", sans-serif;
    position: relative;
  }
  .card {
    position: absolute;
    width: 580px;
    height: 330px;
    background: var(--paper);
    box-shadow: 0 6px 18px rgba(0,0,0,0.18);
    overflow: hidden;
  }
  .card--front { left: 70px; top: 70px; }
  .card--back { left: 550px; top: 500px; }

  .front-pattern {
    position: absolute;
    left: 0; right: 0; top: 90px; bottom: 0;
    background: linear-gradient(180deg, rgba(255,255,255,0) 0%, var(--tint-green) 60%, var(--tint-navy) 100%);
    opacity: 0.45;
  }
  .company-name {
    position: absolute;
    left: 50px; top: 52px;
    font-size: 44px;
    font-weight: 400;
    line-height: 1;
    color: var(--green);
    white-space: nowrap;
  }
  .holder {
    position: absolute;
    left: 222px; top: 178px;
    font-size: 19px;
    font-weight: 700;
    color: var(--navy);
  }
  .address {
    position: absolute;
    left: 40px; top: 250px;
    font-size: 13px;
    line-height: 17px;
    color: var(--grey);
  }
  .contact-list {
    position: absolute;
    list-style: none;
    font-size: 13px;
    line-height: 19px;
    color: var(--grey);
  }
  .contact-list--phones { left: 222px; top: 212px; }
  .contact-list--web { left: 345px; top: 212px; }
  .contact-list li { display: flex; align-items: center; gap: 6px; white-space: nowrap; }
  .contact-list svg { width: 11px; height: 11px; fill: var(--green); flex: none; }

  .back-pattern {
    position: absolute; inset: 0;
    background: linear-gradient(160deg, #dfe6ef 0%, #8fb8a2 35%, #4e74a6 65%, #0f8a45 100%);
  }
  .back-name {
    position: absolute;
    left: 50%; top: 50%;
    transform: translate(-50%, -50%);
    font-size: 36px;
    font-weight: 400;
    color: var(--paper);
    white-space: nowrap;
  }
</style>
</head>
<body>
  <section class="card card--front" aria-label="Card front">
    <div class="front-pattern" role="img" aria-label="Faint tiled brand pattern"></div>
    <p class="company-name">Tallowfen Property Group</p>
    <p class="holder">Gregory L. Hanlon</p>
    <ul class="contact-list contact-list--phones">
      <li><svg viewBox="0 0 12 12"><path d="M2.5 1l2 2-1 1.5c.8 1.6 2 2.8 3.5 3.5L8.5 7l2 2-1.5 2C5 10.5 1.5 7 1 2.5z"/></svg>415-555-0142</li>
      <li><svg viewBox="0 0 12 12"><rect x="3" y="0.5" width="6" height="11" rx="1"/><rect x="4" y="2" width="4" height="6" fill="#fff"/></svg>415-555-0186</li>
      <li><svg viewBox="0 0 12 12"><rect x="3" y="1" width="6" height="4" fill="none" stroke="#0f8a45"/><rect x="1" y="5" width="10" height="6" rx="1"/></svg>415-555-0143</li>
    </ul>
    <ul class="contact-list contact-list--web">
      <li><svg viewBox="0 0 12 12"><rect x="0.5" y="2" width="11" height="8"/><path d="M0.5 2l5.5 4.5L11.5 2" fill="none" stroke="#fff"/></svg>ghanlon@tallowfengroup.example</li>
      <li><svg viewBox="0 0 12 12"><circle cx="6" cy="6" r="5.5"/><path d="M0.5 6h11M6 0.5c-3 3-3 8 0 11M6 0.5c3 3 3 8 0 11" fill="none" stroke="#fff" stroke-width="0.8"/></svg>www.tallowfengroup.example</li>
    </ul>
    <p class="address">782 Marlowe Avenue<br>San Francisco,<br>California 94127</p>
  </section>

  <section class="card card--back" aria-label="Card back">
    <div class="back-pattern" role="img" aria-label="Tiled brand pattern in green and navy"></div>
    <p class="back-name">Tallowfen Property Group</p>
  </section>
</body>
</html>
```